Dog walking/Pet Sitting company needs a brochure to hook high end apartment tenants

We are looking for a brochure design that we can bring to meetings with high-end apartment and hotel management that will explain who we are, what we do, and how we can help their tenants/guests. I would like it to reflect the same look and feel of our website, carried over to printed brochure. Wesbite is www.hollowbrookpawcare.com. I can provide the stock images from the website if needed. A bi-fold brochure is ideal, unless you feel the information would fit better on a tri-fold. My company colors are #5D4664 and #5BA046. I would like a more professional tone to it, rather than fun.

Target Market(s)

Demo Professional Females and Males ages 30-50 with pets

Industry/Entity Type

Pet sitting

Font styles to use
Sans Serif

Colors
6b449b
9bcb3c

Requirements
Must have
• the same look and feel as my website; explain who we are, what we do, how we can help; include services offered; Mention that we service Brindle Hollow and surrounding towns. Mention 15 years in business.
Should not have
• do not list pricing on brochure (you can mention pricing is available on the website). No cartoonish feel.

```html
<!DOCTYPE html>
<html lang="en">
<head>
<meta charset="utf-8">
<title>Hollowbrook Paw Care Tri-fold Brochure</title>
<link href="https://fonts.googleapis.com/css2?family=Montserrat:wght@500;600;700;800&family=Open+Sans:ital,wght@0,400;0,600;1,400&display=swap" rel="stylesheet">
<style>
:root{
  --purple:#5D4664;
  --purple-dark:#3a2841;
  --green:#5BA046;
  --green-light:#8cc63f;
  --ink:#4a4a4a;
  --paper:#ffffff;
  --stage:#eeeeee;
  --photo-warm:#b99a78;
  --photo-cool:#9aa38f;
}
*{box-sizing:border-box;margin:0;padding:0}
html,body{width:753px;height:1200px;overflow:hidden;background:var(--stage)}
body{font-family:"Open Sans",sans-serif;color:var(--ink);position:relative}
.spread{position:absolute;left:45px;width:663px;height:425px;display:grid;grid-template-columns:repeat(3,1fr);background:var(--paper);box-shadow:0 2px 8px rgba(0,0,0,.18)}
.spread--outside{top:45px}
.spread--inside{top:590px}
.spread-label{position:absolute;left:0;width:753px;text-align:center;font-family:"Montserrat",sans-serif;font-weight:700;font-size:13px;letter-spacing:1px;color:#555}
.spread-label--outside{top:488px}
.spread-label--inside{top:1033px}
.panel{position:relative;overflow:hidden;padding:14px 14px}
.panel--dark{background:var(--purple-dark);color:#e6dfe9}
h3{font-family:"Montserrat",sans-serif;font-weight:700;font-size:11px;color:var(--green);margin-bottom:4px;display:flex;align-items:center;gap:5px}
h3 .dot{width:9px;height:9px;border-radius:50%;background:var(--green);flex:none}
p{font-size:6.2px;line-height:1.5;margin-bottom:9px}
.photo{background:linear-gradient(135deg,var(--photo-warm),var(--photo-cool))}
.circle{position:absolute;border-radius:50%;border:4px solid var(--green)}
/* outside */
.mission-photo{width:112px;height:112px;right:10px;bottom:14px}
.ring-accent{position:absolute;border-radius:50%;background:var(--green-light);opacity:.8}
.quotes h3{justify-content:center;color:#fff;margin-bottom:8px}
.quote{font-style:italic;font-size:6px;line-height:1.5;margin-bottom:7px;text-align:center}
.testimonial-photo{width:98px;height:98px;left:61px;top:170px;border-color:var(--paper)}
.contact{position:absolute;left:0;right:0;top:282px;text-align:center;font-size:6.4px;line-height:1.7}
.contact strong{display:block;color:#fff;font-size:7px}
.socials{display:flex;justify-content:center;gap:6px;margin-top:6px}
.socials span{width:9px;height:9px;border-radius:50%;background:var(--green)}
.brand{display:flex;align-items:center;gap:6px;position:absolute;right:14px;top:14px;font-family:"Montserrat",sans-serif;font-weight:800;font-size:11px;color:var(--purple);line-height:1.1;text-align:left;z-index:2}
.brand .mark{width:18px;height:18px;background:var(--purple)}
.cover-photo{position:absolute;left:0;top:0;width:221px;height:260px}
.cover-band{position:absolute;left:0;top:215px;width:221px;height:70px}
.cover-copy{position:absolute;left:0;right:0;top:285px;text-align:center}
.cover-copy .kicker{font-family:"Montserrat",sans-serif;font-weight:600;font-size:10px;color:var(--purple)}
.cover-copy .headline{font-family:"Montserrat",sans-serif;font-weight:800;font-size:21px;line-height:1.1;color:var(--green);margin-top:4px}
.site{position:absolute;left:0;right:0;bottom:12px;text-align:center;font-size:6.5px;font-weight:600;color:var(--purple)}
.panel--dark .site{color:#cfc3d4}
/* inside */
.top-strip{position:absolute;left:0;top:0;width:221px;height:62px}
.years{position:relative;margin-top:58px;text-align:center;color:var(--purple)}
.years small{display:block;font-size:6.5px;line-height:1.4}
.years b{font-family:"Montserrat",sans-serif;font-weight:800;font-size:17px}
.pill{display:block;width:108px;margin:6px 0 8px;background:var(--green);color:#fff;font-family:"Montserrat",sans-serif;font-weight:700;font-size:9px;text-align:center;padding:3px 0;border-radius:0 10px 10px 0;margin-left:-14px}
.service{position:relative;height:82px}
.service .text{width:118px}
.service .text--right{margin-left:85px}
.service .circle{width:70px;height:70px;top:2px;border-width:3px}
.service .circle--right{right:0}
.service .circle--left{left:0}
.dark-photo{height:108px;margin-bottom:10px;border:3px solid var(--green)}
.panel--dark h3{color:#fff;justify-content:center;text-align:center}
.panel--dark p{text-align:center}
.sleep-photo{position:relative;width:84px;height:84px;margin:2px auto 8px;border-radius:50%;border:3px solid var(--green)}
.free-photo{position:absolute;left:0;top:0;width:221px;height:112px}
.free-head{margin-top:104px;text-align:right}
.free-head .small{font-family:"Montserrat",sans-serif;font-weight:600;font-size:9px;color:var(--purple)}
.free-head .big{font-family:"Montserrat",sans-serif;font-weight:800;font-size:18px;color:var(--purple)}
.perk{display:flex;gap:7px;margin-top:9px}
.perk .icon{flex:none;width:20px;height:20px;background:var(--green);border-radius:3px;display:flex;align-items:center;justify-content:center}
.perk h4{font-family:"Montserrat",sans-serif;font-weight:700;font-size:8px;color:var(--purple);margin-bottom:2px}
.perk p{margin-bottom:0;font-size:5.9px}
</style>
</head>
<body>

<section class="spread spread--outside">
  <div class="panel">
    <h3><span class="dot"></span>We're on a Mission</h3>
    <p>For over fifteen years our team has given pets the steady care they deserve while their people work, travel and live full lives. We treat every visit with the same attention we give our own animals, and we keep owners informed at every step so nothing is left to chance.</p>
    <h3><span class="dot"></span>Support Local</h3>
    <p>We are a locally owned business rooted in Brindle Hollow. Choosing us keeps care close to home and supports neighbors who know the streets, parks and buildings your pets call home every day.</p>
    <h3><span class="dot"></span>Life is a Balancing Act</h3>
    <p>Long days and busy weeks should never mean a lonely pet. We fill the gaps with reliable walks and visits so you can focus on work and family with confidence.</p>
    <div class="ring-accent" style="width:60px;height:60px;right:100px;bottom:8px;"></div>
    <div class="circle photo mission-photo" role="img" aria-label="Photo of a happy dog sitting on grass"></div>
  </div>

  <div class="panel panel--dark quotes">
    <h3><span class="dot"></span>What Our Clients Say</h3>
    <p class="quote">“They have cared for our dogs for years and we always come home to calm, happy pets.”</p>
    <p class="quote">“Professional, punctual and kind. The daily photos make my workday so much easier.”</p>
    <p class="quote">“I would not trust anyone else with my cat while I travel.”</p>
    <div class="circle photo testimonial-photo" role="img" aria-label="Photo of a dog with a toy"></div>
    <div class="contact">
      <strong>Brindle Hollow Township</strong>
      555-014-2290<br>
      hello@hollowbrookpawcare.com<br>
      care@hollowbrookpawcare.com<br>
      www.hollowbrookpawcare.com
      <div class="socials"><span></span><span></span><span></span><span></span><span></span></div>
    </div>
  </div>

  <div class="panel">
    <div class="cover-photo photo" role="img" aria-label="Photo of a smiling woman hugging her dog"></div>
    <div class="brand"><span class="mark"></span><span>HOLLOWBROOK<br>PAW CARE</span></div>
    <svg class="cover-band" viewBox="0 0 221 70" preserveAspectRatio="none" aria-hidden="true">
      <path d="M0 40 Q110 0 221 18 L221 70 L0 70 Z" fill="#5BA046"/>
      <path d="M0 52 Q110 14 221 32 L221 70 L0 70 Z" fill="#ffffff"/>
    </svg>
    <div class="cover-copy">
      <div class="kicker">Prioritize Your Family</div>
      <div class="headline">WE'LL FOCUS ON<br>YOUR PETS</div>
    </div>
    <div class="site">www.hollowbrookpawcare.com</div>
  </div>
</section>
<div class="spread-label spread-label--outside">BROCHURE OUTSIDE</div>

<section class="spread spread--inside">
  <div class="panel">
    <div class="top-strip photo" role="img" aria-label="Photo strip of a dog on a walk"></div>
    <div class="years"><small>Proudly servicing Brindle Hollow &amp; surrounding<br>neighborhoods for</small><b>OVER 15 YEARS</b></div>
    <span class="pill">OUR SERVICES</span>
    <div class="service">
      <div class="text"><h3>Dog Walking</h3><p>Daily midday walks that keep dogs active and relaxed while you are at work or away from home.</p></div>
      <div class="circle circle--right photo" role="img" aria-label="Photo of a dog on a leash"></div>
    </div>
    <div class="service">
      <div class="circle circle--left photo" role="img" aria-label="Photo of a dog resting at home"></div>
      <div class="text text--right"><h3>Pet Sitting</h3><p>In-home visits for feeding, play and care so pets stay in their own familiar space.</p></div>
    </div>
    <div class="service">
      <div class="text"><h3>Cat Sitting/<br>Small Pet Sitting</h3><p>Gentle care for cats and small pets, fitted to each routine.</p></div>
      <div class="circle circle--right photo" role="img" aria-label="Photo of a cat"></div>
    </div>
  </div>

  <div class="panel panel--dark">
    <div class="dark-photo photo" role="img" aria-label="Photo of dogs playing together at day care"></div>
    <h3>Day Care &amp; Overnight<br>Boarding</h3>
    <p>Trusted day care and boarding in a calm home setting. Pets enjoy play, rest and attention from caring sitters who follow their usual schedule and needs.</p>
    <div class="sleep-photo photo" role="img" aria-label="Photo of a dog sleeping"></div>
    <h3>Sleepovers</h3>
    <p>Our sitter stays overnight in your home so pets keep their routine and your home stays occupied while you travel. Pricing details are available on our website.</p>
    <div class="site">www.hollowbrookpawcare.com</div>
  </div>

  <div class="panel">
    <div class="free-photo photo" role="img" aria-label="Photo of two dogs outdoors"></div>
    <div class="free-head"><div class="small">Ready To Free Up</div><div class="big">Your Time?</div></div>
    <div class="perk">
      <span class="icon"><svg width="12" height="12" viewBox="0 0 12 12" aria-hidden="true"><path d="M2 6.5l2.5 2.5L10 3" stroke="#fff" stroke-width="1.8" fill="none"/></svg></span>
      <div><h4>Online Registration</h4><p>Sign up in minutes through our secure client portal and share your pet's details.</p></div>
    </div>
    <div class="perk">
      <span class="icon"><svg width="12" height="12" viewBox="0 0 12 12" aria-hidden="true"><path d="M3 1.5h2l1 2.5-1.3 1a6 6 0 0 0 2.3 2.3l1-1.3 2.5 1v2A1.5 1.5 0 0 1 9 10.5 8 8 0 0 1 1.5 3 1.5 1.5 0 0 1 3 1.5z" fill="#fff"/></svg></span>
      <div><h4>Complimentary Consultation</h4><p>Meet your sitter at no cost to review routines, keys and special needs.</p></div>
    </div>
    <div class="perk">
      <span class="icon"><svg width="12" height="12" viewBox="0 0 12 12" aria-hidden="true"><rect x="1.5" y="2.5" width="9" height="8" rx="1" stroke="#fff" stroke-width="1.3" fill="none"/><path d="M1.5 5h9M4 1v3M8 1v3" stroke="#fff" stroke-width="1.3"/></svg></span>
      <div><h4>Flexible Scheduling</h4><p>Book recurring or one-time visits that fit your calendar, with easy changes online.</p></div>
    </div>
    <div class="perk">
      <span class="icon"><svg width="12" height="12" viewBox="0 0 12 12" aria-hidden="true"><rect x="1" y="3" width="10" height="7" rx="1" stroke="#fff" stroke-width="1.3" fill="none"/><circle cx="6" cy="6.5" r="1.8" stroke="#fff" stroke-width="1.2" fill="none"/></svg></span>
      <div><h4>Visits with Reports &amp; Photos</h4><p>Receive a short update and photos after every visit so you always know how your pet is doing.</p></div>
    </div>
  </div>
</section>
<div class="spread-label spread-label--inside">BROCHURE INSIDE</div>

</body>
</html>
```